Flyer für einen Hersteller von Campingzubehör
Zielgruppe
Wir sind Hersteller von Campingzubehör, in der Hauptsache für Wohnmobile und Markisen. Zielgruppe sind daher alle Camper mit entsprechenden Freizeitfahrzeugen. Bei diesem Flyer soll der Camper aufmerksam werden, das der Sonnenschutz individuell bedruckt werden kann, mit eigenen Motiven. Viele lasse sich auf das Sonnensegel eine schöne Urlaubserinnerung, den Hund, oder etwas was dem Camper lieb und wichtig ist. Eben ganz individuell. Wichtig ist das der Sonnenschutz Made in Germany ist! und absolut werkzeugfrei handzuhaben ist. Spezifikationen werden von uns eingefügt.
Aufgabenstellung
Der Flyer soll nach der beiliegenden Druckvorlage erstellt werden. Falzflyer, DIN A5, 4 Seiten. Sinngemäße Angabe in der Vorlage. Auf der 4 Seite soll das Bestellformular erscheinen, also diese Seite bitte freilassen und 'nur' die 3 Seiten gestalten.
Auf der Titelseite soll das auf das 'Schattenproblem' aufmerksam gemacht werden. Ich bin sehr gespannt! Bei Fragen bitte melden. Für den Hintergrund lasse ich dem Designer feien lauf...

```html
<!DOCTYPE html>
<html lang="de">
<head>
<meta charset="utf-8">
<title>Sonnrand Camping – Faltflyer Sunblocker</title>
<link href="https://fonts.googleapis.com/css2?family=Open+Sans:wght@400;600;700&display=swap" rel="stylesheet">
<style>
:root{
  --lime:#e6ef00;
  --green:#8cc63f;
  --grass:#6fae2a;
  --grass-dark:#4d8a1c;
  --sky:#9fd4e6;
  --tree:#5f7a34;
  --ink:#1d1d1b;
  --white:#ffffff;
  --van:#e9ebec;
  --awning-dark:#2b2b2d;
}
*{margin:0;padding:0;box-sizing:border-box}
html,body{width:1200px;height:2534px;overflow:hidden;background:var(--white)}
body{position:relative;font-family:"Open Sans",Arial,sans-serif;color:var(--ink)}
.spread{position:absolute;width:995px;overflow:hidden;box-shadow:0 6px 22px rgba(0,0,0,.35);background:var(--white)}
.spread--one{left:110px;top:60px;height:707px}
.spread--two{left:110px;top:860px;height:710px}
.spread--three{left:120px;top:1672px;height:712px}
.scene{position:absolute;background:linear-gradient(180deg,var(--sky) 0%,#b9d9a0 14%,var(--tree) 24%,#8fc640 36%,var(--grass) 60%,var(--grass-dark) 100%)}
.scene--full{left:0;top:0;width:995px;height:100%}
.curves{position:absolute;left:0;top:0;width:995px;height:100%}
.block{position:absolute}
.van{position:absolute;background:var(--van);border-radius:18px 60px 30px 14px;box-shadow:0 8px 14px rgba(0,0,0,.25)}
.awning{position:absolute;box-shadow:0 6px 12px rgba(0,0,0,.4)}
.awning--black{background:linear-gradient(180deg,#333 0%,var(--awning-dark) 100%)}
.awning--puppy{background:linear-gradient(135deg,#8aa84a 0%,#a8652e 50%,#c9d28a 100%)}
.awning--terrier{background:linear-gradient(135deg,#6b5a45 0%,#e6df7a 55%,#b9b9b9 100%)}
.awning--road{background:linear-gradient(180deg,#4f8fd6 0%,#e8f1fb 45%,#b8a45a 75%,#8b7d4c 100%)}
.awning--sunset{background:linear-gradient(180deg,#365d8f 0%,#1b2a3e 45%,#f2a13a 70%,#2a1a10 100%)}
.awning-caption{position:absolute;left:0;right:0;bottom:8px;text-align:center;color:#d9d9d9;font-size:17px}
.germany{position:absolute;left:40px;top:345px}
.flag{position:absolute;left:0;top:8px;width:36px;height:48px;display:flex;flex-direction:column;transform:skewY(-18deg)}
.flag span{flex:1}
.flag span:nth-child(1){background:#111}
.flag span:nth-child(2){background:#dd0000}
.flag span:nth-child(3){background:#ffce00}
.germany-label{position:absolute;left:44px;top:28px;font-size:14px;line-height:14px;white-space:nowrap}
.germany-label strong{display:block;font-size:20px;line-height:22px;font-weight:700}
.contact{position:absolute;left:84px;top:433px;font-size:13px;line-height:17px}
.contact-title{color:var(--green);font-weight:700;font-size:12px;margin-bottom:1px}
.contact p + p{margin-top:16px}
.brand{position:absolute;display:flex;align-items:center;gap:8px;color:var(--green);font-weight:700;font-size:18px;white-space:nowrap}
.brand i{display:block;width:16px;height:16px;border-radius:50%;background:var(--green)}
.brand--on-white{color:var(--green)}
.headline{position:absolute;left:598px;top:440px;color:var(--ink)}
.headline-new{color:var(--lime);font-weight:700;font-size:54px;line-height:60px;margin-left:73px}
.headline-title{font-size:26px;line-height:34px;margin-top:6px;letter-spacing:.5px}
.headline-sub{font-size:14.5px;line-height:19px;margin-top:16px}
.delivery{position:absolute;left:510px;top:33px;width:210px;font-size:12px;line-height:15px}
.ideas{position:absolute;left:667px;top:118px;font-size:25px;line-height:34px;letter-spacing:.5px}
.features{position:absolute;left:602px;top:224px;list-style:none;font-size:15px;line-height:19.6px}
.features li::before{content:"";display:inline-block;width:8px;height:8px;border-radius:50%;background:var(--lime);margin-right:9px;vertical-align:1px}
.product{position:absolute;left:52px;top:438px;width:400px}
.product-title{color:var(--green);font-size:14.5px;line-height:18px}
.product-text{font-size:11.6px;line-height:15.2px}
.product-price{color:var(--green);font-size:14.5px;margin-top:20px;margin-left:3px}
</style>
</head>
<body>

<!-- Außenseite A -->
<section class="spread spread--one">
  <div class="scene scene--full" role="img" aria-label="Foto einer Wiese mit Bäumen und Himmel, links und rechts je ein weißes Wohnmobil mit ausgefahrenem Sonnensegel"></div>
  <div class="van" style="left:20px;top:82px;width:435px;height:150px"></div>
  <div class="awning awning--black" style="left:158px;top:103px;width:282px;height:185px" role="img" aria-label="Schwarzes Sonnensegel">
    <span class="awning-caption">Auch in schwarz erhältlich</span>
  </div>
  <div class="van" style="left:540px;top:82px;width:440px;height:150px"></div>
  <div class="awning awning--puppy" style="left:560px;top:105px;width:265px;height:180px" role="img" aria-label="Sonnensegel bedruckt mit dem Foto eines Welpen auf einer Blumenwiese"></div>
  <svg class="curves" viewBox="0 0 995 707" preserveAspectRatio="none" aria-hidden="true">
    <path d="M0,318 C265,295 478,445 500,707 L0,707 Z" fill="var(--lime)"/>
    <path d="M0,343 C255,325 462,468 490,707 L0,707 Z" fill="var(--white)"/>
    <path d="M495,707 C512,455 725,325 995,318 L995,707 Z" fill="var(--lime)"/>
    <path d="M505,707 C524,472 735,343 995,340 L995,707 Z" fill="var(--green)"/>
    <path d="M778,707 C778,530 872,420 995,418 L995,707 Z" fill="var(--white)"/>
  </svg>
  <div class="germany"><div class="flag"><span></span><span></span><span></span></div><div class="germany-label">MADE IN<strong>GERMANY</strong></div></div>
  <div class="contact">
    <div class="contact-title">KONTAKT INFORMATION</div>
    <p>Sonnrand Camping UG<br>GF Markus Feldner<br>Wiesenweg 14<br>94123 Talbach</p>
    <p>Tel. 09123 4567890<br>Email: info@sonnrand-camping.de</p>
  </div>
  <div class="brand" style="left:84px;top:597px"><i></i>Sonnrand Camping</div>
  <div class="headline">
    <div class="headline-new">NEU</div>
    <div class="headline-title">BEDRUCKBARE<br>SUNBLOCKER</div>
    <div class="headline-sub">mit Ihren schönsten<br>Urlaubsbildern</div>
  </div>
  <div class="brand brand--on-white" style="left:812px;top:597px"><i></i>Sonnrand<br>Camping</div>
</section>

<!-- Außenseite B -->
<section class="spread spread--two">
  <div class="scene scene--full" role="img" aria-label="Foto einer Wiese mit Bäumen und Himmel, links und rechts je ein weißes Wohnmobil mit ausgefahrenem Sonnensegel"></div>
  <div class="van" style="left:20px;top:82px;width:435px;height:150px"></div>
  <div class="awning awning--black" style="left:158px;top:103px;width:282px;height:185px" role="img" aria-label="Schwarzes Sonnensegel">
    <span class="awning-caption">Auch in schwarz erhältlich</span>
  </div>
  <div class="van" style="left:540px;top:82px;width:440px;height:150px"></div>
  <div class="awning awning--terrier" style="left:545px;top:105px;width:285px;height:197px" role="img" aria-label="Sonnensegel bedruckt mit dem Foto eines kleinen Hundes auf einer gelben Decke"></div>
  <svg class="curves" viewBox="0 0 995 710" preserveAspectRatio="none" aria-hidden="true">
    <path d="M0,320 C265,297 478,447 500,710 L0,710 Z" fill="var(--lime)"/>
    <path d="M0,345 C255,327 462,470 490,710 L0,710 Z" fill="var(--white)"/>
    <path d="M495,710 C512,457 725,327 995,320 L995,710 Z" fill="var(--lime)"/>
    <path d="M505,710 C524,474 735,345 995,342 L995,710 Z" fill="var(--green)"/>
    <path d="M775,710 C775,532 870,422 995,420 L995,710 Z" fill="var(--white)"/>
  </svg>
  <div class="germany" style="top:347px"><div class="flag"><span></span><span></span><span></span></div><div class="germany-label">MADE IN<strong>GERMANY</strong></div></div>
  <div class="contact" style="top:435px">
    <div class="contact-title">KONTAKT INFORMATION</div>
    <p>Sonnrand Camping UG<br>GF Markus Feldner<br>Wiesenweg 14<br>94123 Talbach</p>
    <p>Tel. 09123 4567890<br>Email: info@sonnrand-camping.de</p>
  </div>
  <div class="brand" style="left:84px;top:599px"><i></i>Sonnrand Camping</div>
  <div class="headline" style="left:595px;top:442px">
    <div class="headline-new">NEU</div>
    <div class="headline-title">BEDRUCKBARE<br>SUNBLOCKER</div>
    <div class="headline-sub">mit Ihren schönsten<br>Urlaubsbildern</div>
  </div>
  <div class="brand brand--on-white" style="left:810px;top:599px"><i></i>Sonnrand<br>Camping</div>
</section>

<!-- Innenseite -->
<section class="spread spread--three">
  <div class="scene" style="left:0;top:0;width:495px;height:363px" role="img" aria-label="Foto eines Wohnmobils auf einer Wiese mit Sonnensegel, bedruckt mit Landstraße unter Wolkenhimmel"></div>
  <div class="van" style="left:40px;top:88px;width:435px;height:150px"></div>
  <div class="awning awning--road" style="left:68px;top:107px;width:255px;height:178px" role="img" aria-label="Sonnensegel mit Landschaftsmotiv"></div>

  <svg class="curves" viewBox="0 0 995 712" preserveAspectRatio="none" aria-hidden="true">
    <path d="M498,363 C520,160 730,22 995,12 L995,363 Z" fill="var(--lime)"/>
    <path d="M508,363 C530,178 740,40 995,32 L995,363 Z" fill="var(--green)"/>
    <path d="M773,363 C780,220 870,118 995,110 L995,363 Z" fill="var(--white)"/>
  </svg>
  <p class="delivery">Heringe und Befestigungsmaterial ist selbstverständlich dabei. Auch ist die Tasche im Lieferumfang enthalten.</p>
  <div class="ideas">FÜR<br>EINZIGARTIGE<br>IDEEN</div>
  <ul class="features">
    <li>Sonnenschutz</li>
    <li>Regenschut</li>
    <li>280gqm</li>
    <li>Sichtschutz</li>
    <li>UV Beständig</li>
    <li>mit Ösen</li>
  </ul>
  <div class="brand brand--on-white" style="left:814px;top:288px"><i></i>Sonnrand<br>Camping</div>

  <div class="product">
    <div class="product-title">SUNBLOCKER 3M X 2,2M</div>
    <p class="product-text">Transparentes Meshewebe, das Licht und Luft durchlässt, aber Wärme blockiert. Höhe2,20m und 3m breit. Passt in jede Kederleiste von Talwind, Markiplus oder Solara! Das Meshgewebe ist Wasserfest und hält bis zu 96% der UV Strahlung ab. Nässe ist kein Problem, das Sonnensegel wird kurz geschüttelt und ist sofort trocken! Ein weiterer Nutzen ist, man sieht nicht wer oder ob hinter dem Sonnensegel jemand sitzt, aber man sieht jeden der vorbei geht! Ein Stück mehr Privatsphäre am Campingplatz. Das Sonnensegel wird einfach in die vorhandene Kederleiste von der Markise einziehen und den Schatten genießen. Das untere Ende ist aus PVC und mit 3 Ösen versehen, damit das Segel abgespannt werden kann.</p>
    <div class="product-price">129,00 €</div>
  </div>

  <div class="scene" style="left:494px;top:363px;width:501px;height:349px" role="img" aria-label="Foto eines Wohnmobils auf einer Wiese mit Sonnensegel, bedruckt mit einem Sonnenuntergang am See"></div>
  <div class="van" style="left:540px;top:448px;width:440px;height:150px"></div>
  <div class="awning awning--sunset" style="left:562px;top:468px;width:258px;height:182px" role="img" aria-label="Sonnensegel mit Sonnenuntergangsmotiv"></div>
</section>

</body>
</html>
```